Bref créative
Business cards with logo
Biz cards
Use same font as used in my logo
May use other font
Professional
Marisol Thorne
Vice President
2817 Hollow Birch Lane
Fernbrook, OR
marisol.thorne@quellvex.com
quellvex.com
Medical device contract manufacturing
· FDA Registered – ISO 13485
· Sterile Packaging
· Adhesive Bonding
· Clean Room Assembly
· Laser Welding
· Laser Marking

```html
<!DOCTYPE html>
<html lang="en">
<head>
<meta charset="utf-8">
<title>Quellvex business cards</title>
<link href="https://fonts.googleapis.com/css2?family=Michroma&family=Open+Sans:wght@400;600;700&display=swap" rel="stylesheet">
<style>
  :root {
    --backdrop: #e4e4e2;
    --card-white: #ffffff;
    --brand-red: #d9503c;
    --brand-red-deep: #c94330;
    --divider-grey: #a9abad;
    --ink: #3a3a3c;
    --ink-soft: #7b7d80;
    --on-red: #ffffff;
  }
  * { box-sizing: border-box; margin: 0; padding: 0; }
  html, body { width: 1200px; height: 838px; overflow: hidden; }
  body {
    background: var(--backdrop);
    font-family: "Open Sans", Arial, sans-serif;
    position: relative;
  }
  .card {
    position: absolute;
    width: 560px;
    height: 320px;
    background: var(--card-white);
    box-shadow: 0 6px 18px rgba(0,0,0,0.18);
    overflow: hidden;
  }
  /* Card back: brand mark and web address */
  .card-back { left: 560px; top: 80px; }
  .back-mark {
    position: absolute;
    left: 0; right: 0; top: 108px;
    display: flex; align-items: center; justify-content: center; gap: 14px;
  }
  .mark-dot {
    width: 34px; height: 34px; border-radius: 50%;
    background: var(--brand-red);
  }
  .brand-name {
    font-family: "Michroma", "Open Sans", sans-serif;
    color: var(--ink);
    letter-spacing: 3px;
    text-transform: uppercase;
  }
  .back-mark .brand-name { font-size: 30px; }
  .web-address {
    position: absolute;
    left: 0; right: 0; top: 212px;
    text-align: center;
    font-size: 15px;
    letter-spacing: 4px;
    color: var(--ink);
  }
  .web-address .web-domain { color: var(--brand-red); font-weight: 600; }

  /* Card front: contact side */
  .card-front { left: 80px; top: 438px; }
  .front-logo-strip {
    position: absolute; left: 0; top: 0; bottom: 0; width: 186px;
    background: var(--card-white);
  }
  .front-logo {
    position: absolute;
    left: 93px; top: 160px;
    transform: translate(-50%, -50%) rotate(-90deg);
    display: flex; flex-direction: column; align-items: center; gap: 6px;
    white-space: nowrap;
  }
  .front-logo .logo-row { display: flex; align-items: center; gap: 10px; }
  .front-logo .mark-dot { width: 22px; height: 22px; }
  .front-logo .brand-name { font-size: 20px; }
  .front-tagline { font-size: 8px; letter-spacing: 1px; color: var(--ink-soft); }
  .divider-band {
    position: absolute; left: 186px; top: 0; bottom: 0; width: 14px;
    background: var(--divider-grey);
  }
  .contact-panel {
    position: absolute; left: 200px; top: 0; right: 0; bottom: 0;
    background: linear-gradient(135deg, var(--brand-red) 0%, var(--brand-red-deep) 100%);
    color: var(--on-red);
    padding: 44px 0 0 34px;
  }
  .person-name { font-size: 20px; font-weight: 700; }
  .person-title { font-size: 13px; margin-top: 2px; opacity: 0.95; }
  .contact-list { list-style: none; margin-top: 34px; }
  .contact-list li {
    display: flex; align-items: center; gap: 10px;
    font-size: 11.5px; line-height: 1; height: 21px;
  }
  .contact-icon { width: 13px; height: 13px; flex: none; }
  .contact-icon svg { display: block; width: 13px; height: 13px; }
  .icon-spacer { width: 13px; flex: none; }
</style>
</head>
<body>

<section class="card card-back">
  <div class="back-mark">
    <span class="mark-dot"></span>
    <span class="brand-name">Quellvex</span>
  </div>
  <p class="web-address">www.<span class="web-domain">quellvex</span>.com</p>
</section>

<section class="card card-front">
  <div class="front-logo-strip">
    <div class="front-logo">
      <div class="logo-row">
        <span class="mark-dot"></span>
        <span class="brand-name">Quellvex</span>
      </div>
      <span class="front-tagline">Medical device contract manufacturing</span>
    </div>
  </div>
  <div class="divider-band"></div>
  <div class="contact-panel">
    <h1 class="person-name">Marisol Thorne</h1>
    <p class="person-title">Vice President</p>
    <ul class="contact-list">
      <li>
        <span class="contact-icon"><svg viewBox="0 0 16 16"><path d="M8 1a5 5 0 0 0-5 5c0 4 5 9 5 9s5-5 5-9a5 5 0 0 0-5-5zm0 7a2 2 0 1 1 0-4 2 2 0 0 1 0 4z" fill="#fff"/></svg></span>
        2817 Hollow Birch Lane
      </li>
      <li><span class="icon-spacer"></span>Fernbrook, OR</li>
      <li>
        <span class="contact-icon"><svg viewBox="0 0 16 16"><path d="M4 1.5l2.2 3-1.4 1.6c.8 1.9 2.3 3.4 4.1 4.2l1.6-1.4 3 2.2-1 2.6C7.4 13.4 2.6 8.6 1.5 3.5z" fill="#fff"/></svg></span>
        Tel 555-014-2290
      </li>
      <li>
        <span class="contact-icon"><svg viewBox="0 0 16 16"><rect x="3" y="1.5" width="10" height="4" fill="#fff"/><rect x="1.5" y="6" width="13" height="6" rx="1" fill="#fff"/><rect x="4" y="10" width="8" height="4.5" fill="#fff" stroke="#c94330"/></svg></span>
        Fax 555-014-2291
      </li>
      <li>
        <span class="contact-icon"><svg viewBox="0 0 16 16"><rect x="1.5" y="3.5" width="13" height="9" fill="none" stroke="#fff" stroke-width="1.5"/><path d="M1.5 3.5l6.5 5 6.5-5" fill="none" stroke="#fff" stroke-width="1.5"/></svg></span>
        marisol.thorne@quellvex.com
      </li>
      <li>
        <span class="contact-icon"><svg viewBox="0 0 16 16"><circle cx="8" cy="8" r="6.5" fill="none" stroke="#fff" stroke-width="1.3"/><ellipse cx="8" cy="8" rx="2.8" ry="6.5" fill="none" stroke="#fff" stroke-width="1.1"/><path d="M1.5 8h13" stroke="#fff" stroke-width="1.1"/></svg></span>
        www.quellvex.com
      </li>
    </ul>
  </div>
</section>

</body>
</html>
```